Multivitamin fruit drink in tetrapak

Label design for a 200 ml tetrapak which contains fruit juice with multivitamins in natural form . Product will be promoted to doctors and will follow a otx model. The target is children and women. Being a completely natural fortified multivitamin and mineral drink , the natural aspects to be highlighted. A white background is suggestive . Should not have more than 6 colors as this involves flexo printing.

Target Market(s)

Children and women through doctors recommendations

Industry/Entity Type

Pharmaceutical

Font styles to use
Serif
Sans Serif
Decorative

Requirements
Must have
• Pictures of fruit . Variant 1 is mango and variant 2 is orange. Brand name is Verosta. Can also suggest new names.
Nice to have
• The brand standing out, with white or softer color background
Should not have
• Should not have Dark background. Not funky or too colorful.

```html
<!DOCTYPE html>
<html lang="en">
<head>
<meta charset="utf-8">
<title>Verosta Mango – 200 ml carton label</title>
<link rel="stylesheet" href="https://fonts.googleapis.com/css2?family=Fredoka:wght@600;700&display=swap">
<style>
  :root {
    --orange: #f7a11c;
    --orange-light: #fbbd3e;
    --green: #2e9a45;
    --green-dark: #1f7a34;
    --yellow: #f6c628;
    --red: #d8262b;
    --black: #141414;
    --brown: #2a1f1c;
    --white: #ffffff;
    --leaf: #3f8a3a;
    --mango: #e9952d;
  }
  html, body {
    margin: 0;
    padding: 0;
    width: 1200px;
    height: 2988px;
    overflow: hidden;
    background: var(--white);
  }
  .label {
    position: relative;
    width: 1200px;
    height: 2988px;
    overflow: hidden;
    font-family: "Fredoka", "Arial Rounded MT Bold", sans-serif;
    background: var(--white);
  }
  .band {
    position: absolute;
    left: 0;
    width: 1200px;
    background:
      radial-gradient(circle at 20% 30%, var(--orange-light) 0, transparent 45%),
      radial-gradient(circle at 80% 70%, var(--orange-light) 0, transparent 40%),
      var(--orange);
  }
  .band-top { top: 0; height: 600px; }
  .band-bottom { top: 2120px; height: 868px; }

  .maker-seal {
    position: absolute;
    left: 420px;
    top: 10px;
    width: 360px;
    height: 360px;
    border-radius: 50%;
    background: var(--white);
    border: 18px solid #8fc0e8;
    box-sizing: border-box;
    display: flex;
    align-items: center;
    justify-content: center;
  }
  .maker-name {
    font-weight: 700;
    font-size: 58px;
    color: #1d5aa8;
  }

  .claim-box {
    position: absolute;
    left: 20px;
    top: 688px;
    width: 1080px;
    height: 150px;
    background: var(--green);
    box-shadow: 40px 20px 0 var(--green-dark);
    display: flex;
    align-items: center;
    justify-content: center;
  }
  .claim-text {
    font-weight: 700;
    font-size: 132px;
    color: var(--white);
    letter-spacing: 2px;
  }

  .fruit-art {
    position: absolute;
    left: 0;
    top: 860px;
    width: 1200px;
    height: 1000px;
    background:
      radial-gradient(ellipse 340px 260px at 560px 420px, #f2b43a 0, var(--mango) 45%, rgba(233,149,45,0) 100%),
      radial-gradient(ellipse 700px 480px at 600px 480px, var(--leaf) 0, rgba(63,138,58,0.35) 70%, rgba(255,255,255,0) 100%);
  }

  .natural-ribbon {
    position: absolute;
    left: 110px;
    top: 1570px;
    width: 980px;
    height: 280px;
  }
  .natural-ribbon text {
    font-family: "Fredoka", "Arial Rounded MT Bold", sans-serif;
    font-weight: 700;
    font-size: 118px;
    fill: var(--white);
  }

  .brand-box {
    position: absolute;
    left: 60px;
    top: 1992px;
    width: 1080px;
    height: 170px;
    background: var(--black);
    display: flex;
    align-items: center;
    justify-content: center;
  }
  .brand-name {
    font-weight: 700;
    font-size: 190px;
    line-height: 1;
    color: var(--yellow);
    letter-spacing: 4px;
  }
  .variant-box {
    position: absolute;
    left: 240px;
    top: 2162px;
    width: 720px;
    height: 108px;
    background: var(--brown);
    display: flex;
    align-items: center;
    justify-content: center;
  }
  .variant-name {
    font-weight: 700;
    font-size: 96px;
    line-height: 1;
    color: var(--red);
    letter-spacing: 3px;
  }
  .volume {
    position: absolute;
    right: 20px;
    top: 2858px;
    font-weight: 700;
    font-size: 104px;
    line-height: 1;
    color: var(--white);
  }
</style>
</head>
<body>
<main class="label">
  <div class="band band-top"></div>
  <div class="band band-bottom"></div>

  <div class="maker-seal"><span class="maker-name">Cartova</span></div>

  <div class="claim-box"><span class="claim-text">MULTIVITAMINS</span></div>

  <div class="fruit-art" role="img" aria-label="Illustration of a ripe mango with a sliced piece, set against fanned green mango leaves"></div>

  <svg class="natural-ribbon" viewBox="0 0 980 280" aria-label="100% Natural">
    <path d="M10 60 Q245 10 490 50 T970 40 L960 220 Q735 250 490 230 T20 250 Z" fill="var(--green)"/>
    <path d="M10 60 Q245 10 490 50 T970 40 L960 70 Q735 60 490 80 T14 90 Z" fill="var(--green-dark)" opacity="0.4"/>
    <text x="490" y="185" text-anchor="middle">100% NATURAL</text>
  </svg>

  <div class="brand-box"><span class="brand-name">VEROSTA</span></div>
  <div class="variant-box"><span class="variant-name">MANGO</span></div>

  <div class="volume">200 ML</div>
</main>
</body>
</html>
```